BRISKWATER MOTION GYM FLYER DESIGN

We want a flyer designed for our gym. We have an example of a flyer which we like and I have put it into the images I have uploaded. I would like to recreate using our pictures, so its a pretty straight forward job. We also want to put our weekly timetable on the back of the flyer. We would like the size of the flyer to be A5.

Target Market(s)

FITNESS

Industry/Entity Type

Gym

Colors
33a6d7
ffffff

Requirements
Must have
• We just want to recreate the flyer but we must have the following info on the flyer and we want our timetable on the back of the flyer which you can get from this link: http://www.briskwatermotiongym.com/timetable
• Briskwater Motion Gym is a fun community of humble people. Our goal is to help guide you towards a fitter, healthier lifestyle!
• Our Programs
• HIIT
• High intensity interval training is 30-45 minutes of fat burning fun. The class is a mix of cardio, bodyweight and some resistance movements.
• Conditioning
• A full hour of strength, cardio and bodyweight training to get you in tip top shape. Expect a mix of barbells, kettlebells, rowing machines, bikes and other training methods.
• KPL
• This is our big Friday session to set you up for the weekend. 90 minutes of hard training that is done with a team emphasis. From heavy lifting to cardio triathlons, this class has it all but not for the faint hearted.
• Muay Thai
• Commonly known as the science of 8 limbs you will learn how to punch, kick, knee and elbow. Thailands national sport is a great way to get your fitness kick. We train the complete beginner all the way to international fighters so you are in great hands.
• Kids Muay Thai
• Our junior program starts from age 6 onwards. Muay Thai is a great way for kids to get active and fit while learning new skills. Training in martial arts also teaches self discipline and socialisation skills.
• Yoga
• A combination of physical and mental practises that will leave you focused and refreshed for whatever the week throws at you. We always recommend our yoga classes as a great way to balance the high intensity training we offer.
• U-Press
• Strength training with a little bit of conditioning. We regularly update the program and re test lifts to ensure you are making progress and getting stronger.
• CONTACT US
• OUR LOCATION:
• Unit 42C
• 273 Quillan Street
• Fenwick Hollow
• Glasgow
• G72TR
• Phone: 07950362814
• Email: info@briskwatermotiongym.com
• Web: www.briskwatermotiongym.com
Nice to have
• Can use all the picture but if not be good to use the boxing one and the group training one.

```html
<!DOCTYPE html>
<html lang="en">
<head>
<meta charset="utf-8">
<title>Briskwater Motion Gym – Flyer</title>
<link rel="stylesheet" href="https://fonts.googleapis.com/css2?family=Titillium+Web:wght@300;400;600;700&display=swap">
<style>
  :root {
    --sky: #49d2eb;
    --teal: #3b8fa1;
    --deep: #1f4f5c;
    --white: #ffffff;
    --paper: #ffffff;
  }
  * { box-sizing: border-box; margin: 0; padding: 0; }
  html, body { width: 960px; height: 1200px; overflow: hidden; background: var(--paper); }
  body { font-family: "Titillium Web", sans-serif; color: var(--deep); }

  .sheet { position: relative; width: 1200px; height: 1500px; transform: scale(0.8); transform-origin: 0 0; }

  .page { position: absolute; left: 110px; width: 981px; height: 692px; background: var(--sky); overflow: hidden; }
  .page--front { top: 35px; }
  .page--back { top: 762px; }
  .layer { position: absolute; left: 0; top: 0; width: 981px; height: 692px; }

  .brand { position: absolute; left: 30px; top: 50px; width: 232px; text-align: center;
    font-size: 23px; font-weight: 700; line-height: 1.05; color: var(--deep); letter-spacing: 1px; }

  .intro { position: absolute; left: 29px; top: 177px; width: 200px; font-size: 10px; line-height: 1.25; color: var(--white); }
  .intro p + p { margin-top: 10px; }
  .intro strong { color: var(--sky); font-weight: 700; }

  .join { position: absolute; left: 87px; top: 307px; }
  .join__title { font-size: 14px; font-weight: 600; color: var(--deep); letter-spacing: .3px; }
  .join__web { font-size: 13px; color: var(--white); margin-top: -2px; }

  .programs-title { position: absolute; left: 320px; top: 372px; font-size: 26px; font-weight: 300; color: var(--deep); letter-spacing: .3px; }
  .programs-title b { font-weight: 700; }

  .program { position: absolute; width: 290px; padding-left: 15px; }
  .program__icon { position: absolute; left: -5px; top: 4px; width: 14px; height: 14px; border: 1.5px solid var(--deep); border-radius: 50%; }
  .program__icon::after { content: ""; position: absolute; left: 4px; top: 3px; width: 3px; height: 5px; background: var(--deep); border-radius: 1px; }
  .program__line { position: absolute; left: 1px; top: 20px; width: 1px; height: 30px; background: var(--deep); opacity: .6; }
  .program h3 { font-size: 17px; font-weight: 600; line-height: 1.1; color: var(--deep); letter-spacing: .2px; }
  .program p { font-size: 8.6px; line-height: 1.38; color: var(--deep); margin-top: 2px; }

  .contact-bar { position: absolute; left: 292px; top: 652px; width: 689px; height: 40px; background: var(--teal);
    display: flex; align-items: center; padding-left: 25px; gap: 14px; font-size: 9.5px; letter-spacing: .8px; color: var(--white); }
  .contact-bar__label { color: var(--sky); font-weight: 700; }
  .contact-bar__item { display: flex; align-items: center; gap: 5px; }
  .contact-bar svg { width: 10px; height: 10px; fill: var(--sky); }

  .timetable-title { position: absolute; left: 47px; top: 42px; font-size: 26px; font-weight: 300; color: var(--white); letter-spacing: .3px; }
  .timetable-title b { color: var(--sky); font-weight: 700; }

  .timetable { position: absolute; left: 47px; top: 196px; width: 887px; height: 448px; border-collapse: collapse; table-layout: fixed; }
  .timetable th, .timetable td { border: 2px solid var(--white); text-align: center; vertical-align: middle; }
  .timetable thead th { height: 30px; font-size: 14px; font-weight: 300; color: var(--white); letter-spacing: .3px; }
  .timetable th.time-col { width: 80px; }
  .timetable tbody th { font-size: 15px; font-weight: 300; color: var(--white); }
  .timetable td { font-size: 8.6px; font-weight: 700; color: var(--deep); line-height: 1.1; letter-spacing: .2px; }
</style>
</head>
<body>
<div class="sheet">

  <!-- Front -->
  <section class="page page--front">
    <svg class="layer" viewBox="0 0 981 692" aria-hidden="true">
      <polygon points="0,165 292,78 292,220 0,305" fill="var(--deep)"/>
      <polygon points="150,122 292,78 292,220" fill="var(--teal)"/>
      <polygon points="0,305 170,375 0,450" fill="var(--teal)"/>
      <polygon points="710,235 981,150 981,330" fill="var(--teal)"/>
    </svg>
    <svg class="layer" viewBox="0 0 981 692" role="img" aria-label="Photo: Muay Thai pad work between a coach and a fighter in the ring">
      <defs>
        <linearGradient id="ringTone" x1="0" y1="0" x2="1" y2="1">
          <stop offset="0" stop-color="#3a2e2c"/>
          <stop offset=".5" stop-color="#7a6258"/>
          <stop offset="1" stop-color="#a88a72"/>
        </linearGradient>
      </defs>
      <polygon points="292,0 981,0 981,150 292,360" fill="url(#ringTone)"/>
    </svg>
    <svg class="layer" viewBox="0 0 981 692" role="img" aria-label="Photo: athlete training with a kettlebell in the gym">
      <defs>
        <linearGradient id="gymTone" x1="0" y1="0" x2="1" y2="1">
          <stop offset="0" stop-color="#2a3340"/>
          <stop offset=".6" stop-color="#3d4550"/>
          <stop offset="1" stop-color="#1d2127"/>
        </linearGradient>
      </defs>
      <polygon points="0,450 292,360 292,692 0,692" fill="url(#gymTone)"/>
    </svg>

    <div class="brand">BRISKWATER<br>MOTION GYM</div>

    <div class="intro">
      <p>Briskwater Motion Gym is a fun community of humble people.</p>
      <p>Our goal is to help guide you towards a <strong>fitter, healthier lifestyle!</strong></p>
    </div>

    <div class="join">
      <div class="join__title">JOIN THE FAMILY</div>
      <div class="join__web">www.briskwatermotiongym.com</div>
    </div>

    <h2 class="programs-title">OUR <b>PROGRAMS</b></h2>

    <article class="program" style="left:330px; top:430px;">
      <span class="program__icon"></span><span class="program__line"></span>
      <h3>HIIT</h3>
      <p>High intensity interval training is 30-45 minutes of fat burning fun. The class is a mix of cardio, bodyweight and some resistance movements.</p>
    </article>
    <article class="program" style="left:330px; top:488px;">
      <span class="program__icon"></span><span class="program__line"></span>
      <h3>CONDITIONING</h3>
      <p>A full hour of strength, cardio and bodyweight training to get you in tip top shape. Expect a mix of barbells, kettlebells, rowing machines, bikes and other training methods.</p>
    </article>
    <article class="program" style="left:330px; top:559px;">
      <span class="program__icon"></span><span class="program__line"></span>
      <h3>KPL</h3>
      <p>This is our big Friday session to set you up for the weekend. 90 minutes of hard training that is done with a team emphasis. From heavy lifting to cardio triathlons, this class has it all but not for the faint hearted.</p>
    </article>

    <article class="program" style="left:659px; top:323px;">
      <span class="program__icon"></span><span class="program__line"></span>
      <h3>MUAY THAI</h3>
      <p>Commonly known as the science of 8 limbs you will learn how to punch, kick, knee and elbow. Thailands national sport is a great way to get your fitness kick. We train the complete beginner all the way to international fighters so you are in great hands.</p>
    </article>
    <article class="program" style="left:659px; top:405px;">
      <span class="program__icon"></span><span class="program__line"></span>
      <h3>KIDS MUAY THAI</h3>
      <p>Our junior program starts from age 6 onwards. Muay Thai is a great way for kids to get active and fit while learning new skills. Training in martial arts also teaches self discipline and socialisation skills.</p>
    </article>
    <article class="program" style="left:659px; top:475px;">
      <span class="program__icon"></span><span class="program__line"></span>
      <h3>YOGA</h3>
      <p>A combination of physical and mental practises that will leave you focused and refreshed for whatever the week throws at you. We always recommend our yoga classes as a great way to balance the high intensity training we offer.</p>
    </article>
    <article class="program" style="left:659px; top:557px;">
      <span class="program__icon"></span><span class="program__line"></span>
      <h3>U-PRESS</h3>
      <p>Strength training with a little bit of conditioning. We regularly update the program and re test lifts to ensure you are making progress and getting stronger.</p>
    </article>

    <footer class="contact-bar">
      <span class="contact-bar__label">CONTACT</span>
      <span>Unit 42C, 273 Quillan Street, Fenwick Hollow, Glasgow G72TR</span>
      <span class="contact-bar__item">
        <svg viewBox="0 0 10 10" aria-hidden="true"><path d="M2 0.5 L3.6 0.5 L4.3 2.8 L3.2 3.8 C3.8 5 4.9 6.1 6.2 6.8 L7.2 5.7 L9.5 6.4 L9.5 8 C9.5 9 8.8 9.5 8 9.5 C4 9.2 0.8 6 0.5 2 C0.5 1.2 1 0.5 2 0.5 Z"/></svg>
        07950362814
      </span>
      <span class="contact-bar__item">
        <svg viewBox="0 0 10 10" aria-hidden="true"><path d="M0.5 2 H9.5 V8.5 H0.5 Z M0.8 2.3 L5 5.6 L9.2 2.3" fill="var(--sky)" stroke="var(--teal)" stroke-width=".7"/></svg>
        info@briskwatermotiongym.com
      </span>
    </footer>
  </section>

  <!-- Back -->
  <section class="page page--back">
    <svg class="layer" viewBox="0 0 981 692" aria-hidden="true">
      <polygon points="0,0 915,0 0,157" fill="var(--deep)"/>
      <polygon points="735,33 981,0 981,172" fill="var(--teal)"/>
    </svg>

    <h2 class="timetable-title">WEEKLY <b>TIMETABLE</b></h2>

    <table class="timetable">
      <thead>
        <tr><th class="time-col"></th><th>MONDAY</th><th>TUESDAY</th><th>WEDNESDAY</th><th>THURSDAY</th><th>FRIDAY</th><th>SATURDAY</th></tr>
      </thead>
      <tbody>
        <tr><th>06:00</th><td></td><td>U-PRESS</td><td>STRENGTH &amp; CONDITIONING</td><td></td><td>U-PRESS</td><td></td></tr>
        <tr><th>07:00</th><td>CONDITIONING</td><td>FIGHT CAMP MUAY THAI</td><td>YOGA 5/25</td><td>CONDITIONING</td><td>FIGHT CAMP MUAY THAI</td><td></td></tr>
        <tr><th>08:00</th><td>OPEN GYM</td><td>OPEN GYM</td><td>OPEN GYM</td><td>OPEN GYM</td><td>OPEN GYM</td><td></td></tr>
        <tr><th>09:00</th><td></td><td></td><td></td><td></td><td></td><td></td></tr>
        <tr><th>10:00</th><td>U-PRESS</td><td></td><td>U-PRESS</td><td></td><td>U-PRESS</td><td>SATURDAY CIRCUIT</td></tr>
        <tr><th>11:00</th><td></td><td></td><td></td><td></td><td></td><td>OPEN GYM /<br>FUNDAMENTALS / KIDS</td></tr>
        <tr><th>12:00</th><td>LUNCHTIME HIIT</td><td>LUNCHTIME HIIT</td><td></td><td>LUNCHTIME HIIT</td><td>LUNCHTIME HIIT</td><td>MUAY THAI FOUNDATIONS</td></tr>
        <tr><th>13:00</th><td></td><td></td><td></td><td></td><td></td><td></td></tr>
        <tr><th>14:00</th><td></td><td></td><td></td><td></td><td></td><td></td></tr>
        <tr><th>15:00</th><td></td><td></td><td></td><td></td><td></td><td></td></tr>
        <tr><th>16:00</th><td>OPEN GYM</td><td>OPEN GYM</td><td>OPEN GYM</td><td>OPEN GYM</td><td>OPEN GYM</td><td></td></tr>
        <tr><th>17:00</th><td>FUNDAMENTALS</td><td>HIIT 30/30</td><td>HIIT 8/30</td><td>HIIT 10/30</td><td></td><td></td></tr>
        <tr><th>18:00</th><td>MUAY THAI FOUNDATIONS</td><td>CONDITIONING &nbsp;/&nbsp; KIDS</td><td>FUNDAMENTALS /<br>MUAY THAI FOUNDATIONS</td><td>CONDITIONING</td><td>U-PRESS</td><td></td></tr>
        <tr><th>19:00</th><td>STRENGTH &amp; CONDITIONING</td><td>MUAY THAI INTERMEDIATE</td><td>YOGA 4/25</td><td>MUAY THAI INTERMEDIATE</td><td>KPL</td><td></td></tr>
      </tbody>
    </table>
  </section>

</div>
</body>
</html>
```